Physiotherapiepraxis braucht Druckvorlage für Werbeanzeige
Zielgruppe
Dienstleistung im Gesundheitswesen als Physiotherapiepraxis.
Krankengymnastik, auch im häuslichen Bereich oder im Altersheim, und Massage sowie Wellnessanwendungen.
Zielgruppe sind primär Erwachsene, eingeschränkt auch Kinder.
Aufgabenstellung
Ich möchte eine Druckvorlage für eine Werbeanzeige, die ich immer mal wieder in verschiedenen Festschriften im dörflichen Bereich oder in einer regionalen Zeitschrift veröffentlichen kann.
Die Anzeige soll das Logo enthalten und die Anschrift der Praxis sowie die Telefonnummer und Adresse der Homepage.

```html
<!DOCTYPE html>
<html lang="de">
<head>
<meta charset="utf-8">
<title>Physiotherapie Hannelore Weskamp – Anzeige</title>
<link rel="stylesheet" href="https://fonts.googleapis.com/css2?family=Open+Sans:wght@400;700&family=Shadows+Into+Light+Two&display=swap">
<style>
  :root {
    --green: #1c7a3b;
    --gold: #d2b82c;
    --white: #ffffff;
    --frame: #9a9a9a;
  }
  * { margin: 0; padding: 0; box-sizing: border-box; }
  html, body { width: 1200px; height: 1200px; overflow: hidden; background: var(--white); }
  .ad {
    position: relative;
    width: 1200px;
    height: 1200px;
    background: var(--white);
    border: 3px solid var(--frame);
    font-family: "Open Sans", Arial, sans-serif;
  }
  .practice-name {
    position: absolute;
    top: 150px;
    left: 0;
    width: 100%;
    display: flex;
    justify-content: center;
    align-items: center;
    gap: 40px;
    color: var(--green);
    font-size: 76px;
    font-weight: 400;
    letter-spacing: 8px;
    line-height: 1;
    white-space: nowrap;
  }
  .practice-name .dot {
    width: 34px;
    height: 34px;
    border-radius: 50%;
    background: var(--gold);
    flex: none;
  }
  .service-band {
    position: absolute;
    top: 325px;
    left: 128px;
    width: 944px;
    height: 152px;
    background: var(--gold);
    color: var(--white);
    font-weight: 700;
    font-size: 100px;
    letter-spacing: 1px;
    display: flex;
    align-items: center;
    justify-content: center;
    white-space: nowrap;
  }
  .info-box {
    position: absolute;
    top: 512px;
    left: 71px;
    width: 1058px;
    height: 615px;
    border: 7px solid var(--green);
  }
  .slogan {
    position: absolute;
    top: 34px;
    left: 42px;
    color: var(--green);
    font-family: "Shadows Into Light Two", cursive;
    font-size: 92px;
    line-height: 122px;
    white-space: nowrap;
  }
  .contact {
    position: absolute;
    top: 322px;
    left: 42px;
    list-style: none;
    color: var(--green);
    font-size: 54px;
    line-height: 80px;
    white-space: nowrap;
  }
  .contact li { display: flex; align-items: center; gap: 14px; }
  .contact svg { width: 38px; height: 38px; flex: none; fill: var(--green); }
</style>
</head>
<body>
  <div class="ad">
    <div class="practice-name">
      <span>Hannelore</span>
      <span class="dot"></span>
      <span>Weskamp</span>
    </div>

    <div class="service-band">PHYSIOTHERAPIE</div>

    <div class="info-box">
      <p class="slogan">Wir bringen Sie schnell<br>wieder auf die Beine</p>

      <ul class="contact">
        <li>
          <svg viewBox="0 0 24 24" aria-hidden="true"><path d="M12 1.5a7.5 7.5 0 0 0-7.5 7.5c0 5.6 7.5 13.5 7.5 13.5s7.5-7.9 7.5-13.5A7.5 7.5 0 0 0 12 1.5zm0 10.5a3 3 0 1 1 0-6 3 3 0 0 1 0 6z"/></svg>
          <span>Lindenweg 7 in 21493 Elmhorst</span>
        </li>
        <li>
          <svg viewBox="0 0 24 24" aria-hidden="true"><path d="M6.6 10.8a15.1 15.1 0 0 0 6.6 6.6l2.2-2.2a1 1 0 0 1 1-.25 11.4 11.4 0 0 0 3.6.57 1 1 0 0 1 1 1V20a1 1 0 0 1-1 1A17 17 0 0 1 3 4a1 1 0 0 1 1-1h3.5a1 1 0 0 1 1 1c0 1.25.2 2.450.57 3.57a1 1 0 0 1-.25 1z"/></svg>
          <span>+49 (0) 4155 - 48 27 16</span>
        </li>
        <li>
          <svg viewBox="0 0 24 24" aria-hidden="true"><path d="M12 2a10 10 0 1 0 0 20 10 10 0 0 0 0-20zm-1 17.9A8 8 0 0 1 4.1 13H7c.1 2.6 1.4 5 4 6.9zM4.1 11A8 8 0 0 1 11 4.1C8.6 6 7.1 8.4 7 11zM13 4.1A8 8 0 0 1 19.9 11H17c-.1-2.6-1.6-5-4-6.9zM11 6.5V11H9c.1-1.7.8-3.2 2-4.5zm2 0c1.2 1.3 1.9 2.8 2 4.5h-2zM11 13v4.5c-1.2-1.3-1.9-2.8-2-4.5zm2 0h2c-.1 1.7-.8 3.2-2 4.5zm0 6.9c2.6-1.9 3.9-4.3 4-6.9h2.9a8 8 0 0 1-6.9 6.9z"/></svg>
          <span>www.physiotherapie-elmhorst.de</span>
        </li>
      </ul>
    </div>
  </div>
</body>
</html>
```